Business Cards - New Logo Rebranding

Hello We know have a red and blue logo and are looking to create new cards. We are looking for the best creativity of the new logo merged with some of the existing artwork provided.

Target Market(s)

Realtors

Industry/Entity Type

Real Estate

Contact Information for Business Card

New logo with rebranded colors

Requirements
Must have
• Creative use of the new logo

```html
<!DOCTYPE html>
<html lang="en">
<head>
<meta charset="utf-8">
<title>Summit Crest Inspection Professionals – Business Card</title>
<link href="https://fonts.googleapis.com/css2?family=Montserrat:wght@400;500;600;700;800&display=swap" rel="stylesheet">
<style>
  :root{
    --brand-blue:#1567b8;
    --brand-blue-deep:#0f5aa6;
    --brand-red:#e0313b;
    --ink:#2b2b2b;
    --paper:#ffffff;
    --backdrop:#e6e6e6;
  }
  *{box-sizing:border-box;margin:0;padding:0}
  html,body{width:1200px;height:1059px;overflow:hidden}
  body{background:var(--backdrop);font-family:"Montserrat",sans-serif;position:relative;color:var(--ink)}

  .card{position:absolute;left:255px;width:690px;height:392px;border-radius:18px;overflow:hidden}
  .card-front{top:100px;background:var(--paper)}
  .card-back{top:537px;background:var(--brand-blue-deep)}

  /* front */
  .brand-mark{position:absolute;left:104px;top:36px;width:84px;height:84px;border-radius:50%;background:var(--brand-blue);border:5px solid var(--brand-red)}
  .brand-name{position:absolute;left:39px;top:122px;width:216px;text-align:center;font-weight:800;font-size:24px;letter-spacing:.5px;color:var(--brand-blue)}
  .brand-tagline{position:absolute;left:39px;top:151px;width:216px;text-align:center;font-weight:600;font-size:8px;letter-spacing:.3px;color:var(--brand-blue)}
  .brand-tagline::before,.brand-tagline::after{content:"";display:inline-block;width:36px;height:1.5px;background:var(--brand-blue);vertical-align:middle;margin:0 5px}

  .name-flag{position:absolute;left:0;top:192px;width:20px;height:40px;background:var(--brand-red)}
  .person-name{position:absolute;left:39px;top:186px;font-weight:800;font-size:26px;color:var(--brand-blue);letter-spacing:.2px}
  .person-name .surname{color:var(--brand-red)}
  .person-title{position:absolute;left:40px;top:218px;font-size:16px;font-weight:500;color:var(--ink)}
  .title-rule{position:absolute;left:238px;top:228px;width:409px;height:1.5px;background:var(--brand-red)}
  .portrait{position:absolute;left:467px;top:26px;width:180px;height:202px;background:linear-gradient(180deg,#f3f5f8 0%,#dfe6ef 45%,#1d5fb5 70%,#1a55a8 100%);border-radius:90px 90px 0 0}

  .contact-list{position:absolute;left:38px;top:254px;list-style:none}
  .contact-list li{display:flex;align-items:center;height:26px;font-size:17px;font-weight:500;color:var(--ink)}
  .contact-list svg{width:18px;height:18px;margin-right:8px;flex:none}

  .service-list{position:absolute;left:417px;top:305px;font-size:17px;font-weight:500;color:var(--ink);line-height:26px}
  .service-list .dot{color:var(--brand-red);margin:0 4px 0 0;font-size:12px;vertical-align:middle}

  .front-rule{position:absolute;left:0;bottom:22px;width:100%;height:2px;background:var(--brand-red)}
  .front-band{position:absolute;left:0;bottom:0;width:100%;height:18px;background:var(--brand-blue)}

  /* back */
  .back-glow{position:absolute;left:25px;top:-10px;width:640px;height:430px;border-radius:50%;border:40px solid rgba(255,255,255,.04)}
  .back-headline{position:absolute;left:0;top:36px;width:100%;text-align:center;font-weight:800;font-size:27px;color:#fff;letter-spacing:.2px}
  .ribbon-rule{position:absolute;left:0;top:111px;width:100%;height:2px;background:var(--brand-red)}
  .ribbon{position:absolute;left:170px;top:93px;width:353px;height:37px;border-radius:19px;background:var(--brand-red);color:#fff;font-size:22px;font-weight:600;text-align:center;line-height:37px}

  .benefits{position:absolute;list-style:none;color:#fff;font-size:16.5px;font-weight:600;line-height:23px}
  .benefits li{position:relative;padding-left:0;margin-bottom:7px}
  .benefits li::before{content:"";position:absolute;left:-14px;top:10px;width:4px;height:4px;border-radius:50%;background:var(--brand-red)}
  .benefits-left{left:42px;top:156px;width:330px}
  .benefits-right{left:384px;top:156px;width:295px}
  .benefits-right li{margin-bottom:9px}

  .credentials{position:absolute;left:0;top:0;width:690px;height:392px;pointer-events:none}
</style>
</head>
<body>

<section class="card card-front">
  <div class="brand-mark"></div>
  <div class="brand-name">SUMMIT CREST</div>
  <div class="brand-tagline">INSPECTION PROFESSIONALS</div>

  <div class="name-flag"></div>
  <h1 class="person-name">DANA <span class="surname">MARLOWE</span></h1>
  <p class="person-title">Certified Mold Inspector</p>
  <div class="title-rule"></div>
  <div class="portrait" role="img" aria-label="Portrait photo of the inspector in a blue company polo shirt"></div>

  <ul class="contact-list">
    <li><svg viewBox="0 0 24 24"><path fill="#1567b8" d="M6.6 10.8a15.1 15.1 0 0 0 6.6 6.6l2.2-2.2a1 1 0 0 1 1-.25 11.4 11.4 0 0 0 3.6.6 1 1 0 0 1 1 1V20a1 1 0 0 1-1 1A17 17 0 0 1 3 4a1 1 0 0 1 1-1h3.5a1 1 0 0 1 1 1c0 1.25.2 2.45.6 3.6a1 1 0 0 1-.25 1z"/></svg>800.555.0142</li>
    <li><svg viewBox="0 0 24 24"><rect x="6" y="2" width="12" height="20" rx="2" fill="none" stroke="#1567b8" stroke-width="2"/><circle cx="12" cy="18" r="1.2" fill="#1567b8"/></svg>562.555.0187</li>
    <li><svg viewBox="0 0 24 24"><rect x="2" y="5" width="20" height="14" fill="#1567b8"/><path d="M2 5l10 8 10-8M2 19l7-7M22 19l-7-7" fill="none" stroke="#fff" stroke-width="1.5"/></svg>dana.marlowe@summitcrestinspect.com</li>
    <li><svg viewBox="0 0 24 24"><g fill="none" stroke="#1567b8" stroke-width="1.6"><circle cx="12" cy="12" r="10"/><ellipse cx="12" cy="12" rx="4.5" ry="10"/><path d="M2 12h20M4 7h16M4 17h16"/></g></svg>www.SummitCrestInspect.com</li>
  </ul>

  <div class="service-list">
    <div><span class="dot">•</span>Home <span class="dot">•</span>Sewer <span class="dot">•</span>Mold <span class="dot">•</span>Roof</div>
    <div><span class="dot">•</span>Commercial <span class="dot">•</span>Termite</div>
  </div>

  <div class="front-rule"></div>
  <div class="front-band"></div>
</section>

<section class="card card-back">
  <div class="back-glow"></div>
  <h2 class="back-headline">CALIFORNIA’S #1 INSPECTION COMPANY!</h2>
  <div class="ribbon-rule"></div>
  <div class="ribbon">Why Choose Summit Crest</div>

  <ul class="benefits benefits-left">
    <li>Performing Inspections Since 1984</li>
    <li>HomeCert Certified Master /<br>Professional Inspectors®</li>
    <li>500,000+ Inspections Completed Statewide</li>
    <li>90-Day Inspection Guarantees</li>
  </ul>
  <ul class="benefits benefits-right">
    <li>Request of Repairs Pricer Report</li>
    <li>AeroBoard Drone Licensed Roof Inspectors upon request</li>
    <li>5,000+ 5-Star Reviews on Searchly &amp; Ratewise</li>
  </ul>

  <svg class="credentials" viewBox="0 0 690 392" aria-label="Certification and listing badges">
    <circle cx="357" cy="353" r="18" fill="#ffffff" stroke="#e0313b" stroke-width="3"/>
    <circle cx="410" cy="353" r="18" fill="#d6b24a" stroke="#a8862c" stroke-width="2"/>
    <circle cx="461" cy="353" r="18" fill="#cfc8ae" stroke="#9c9479" stroke-width="2"/>
    <rect x="496" y="333" width="2" height="38" fill="#e0313b"/>
    <circle cx="528" cy="353" r="14" fill="#d6b24a"/>
    <rect x="536" y="343" width="42" height="20" fill="#1e3f8f" stroke="#d6b24a" stroke-width="1"/>
    <rect x="590" y="340" width="42" height="26" rx="3" fill="#ffffff"/>
    <circle cx="660" cy="350" r="10" fill="none" stroke="#ffffff" stroke-width="4"/>
  </svg>
</section>

</body>
</html>
```